Veltora Software Business Card Design

We are a new organization called Veltora. We are a software as a service provider. We deliver a project and program management solution via the internet, so everyone has the ability to work together and collaborate. Its an enterprise platform and we will focus on 50 plus employee company.

We have a website in place
www.veltora-demo.com

Use this as a start of producing the business card. The logo is there as well, but if you have a great and better solution...

Color scheme's could be inline with the website, but don't pin point on it. We can always change the website, logo, color scheme etc.

Target Market(s)

B2B, Projectmembers, projectmanagers, ICT, CTO, Marketing Managers

Industry/Entity Type

Software

Requirements
Must have
• Marten Kuyvelsma

Tel: +31 255 47 09 36
Mob: +31 6 927 15 062
marten@veltora-demo.com
Oostelingpad 84c
2184 KT Nieuw Vennep

Www.veltora-demo.com
social media links

```html
<!DOCTYPE html>
<html lang="en">
<head>
<meta charset="utf-8">
<title>Veltora Business Card</title>
<link href="https://fonts.googleapis.com/css2?family=Cabin:ital,wght@0,400;0,500;0,600;1,400&display=swap" rel="stylesheet">
<style>
  :root {
    --page: #e6e7e8;
    --card: #ffffff;
    --lime: #b3c124;
    --lime-soft: #bccf3c;
    --blue: #1ea5e6;
    --orange: #f2900f;
    --ink: #3a3a3a;
    --ink-soft: #555555;
    --white: #ffffff;
  }
  * { box-sizing: border-box; margin: 0; padding: 0; }
  html, body {
    width: 1200px; height: 900px; overflow: hidden;
    background: var(--page);
    font-family: "Cabin", sans-serif;
    color: var(--ink);
  }
  .canvas { position: relative; width: 1200px; height: 900px; }

  .card {
    position: absolute; left: 250px; width: 700px; height: 400px;
    box-shadow: 0 6px 18px rgba(0,0,0,.18);
    overflow: hidden;
  }

  /* Back side */
  .card-back { top: 40px; background: var(--lime); }
  .card-back .brand-name {
    position: absolute; left: 0; right: 0; top: 150px;
    text-align: center; color: var(--white);
    font-size: 76px; font-weight: 400; letter-spacing: 1px;
  }
  .card-back .web {
    position: absolute; left: 0; right: 0; bottom: 32px;
    text-align: center; color: var(--white); font-size: 12px;
  }

  /* Front side */
  .card-front { top: 470px; background: var(--card); }
  .brand-band {
    position: absolute; left: 140px; top: 38px; width: 290px; height: 104px;
    background: var(--lime); border-radius: 0 16px 16px 0;
    display: flex; align-items: center; padding-left: 24px;
  }
  .brand-band .brand-name {
    color: var(--white); font-size: 62px; font-weight: 400; letter-spacing: 1px;
  }

  .role {
    position: absolute; width: 92px; height: 92px; border-radius: 50%;
    display: flex; align-items: center; justify-content: center; text-align: center;
    color: var(--white); font-size: 10px; font-weight: 600; line-height: 1.25;
    text-transform: uppercase; letter-spacing: .3px;
    box-shadow: 0 2px 4px rgba(0,0,0,.15);
  }
  .role-team { left: 62px; top: 160px; background: var(--blue); }
  .role-pm { left: 176px; top: 198px; background: var(--orange); }
  .role-mgmt { left: 298px; top: 236px; background: var(--lime-soft); }

  .greeting {
    position: absolute; left: 448px; top: 48px;
    font-size: 12px; font-style: italic; color: var(--ink-soft);
  }
  .person-name {
    position: absolute; left: 448px; top: 92px;
    font-size: 22px; font-weight: 400; letter-spacing: 1px; text-transform: uppercase;
  }
  .contact-list {
    position: absolute; left: 448px; top: 134px; list-style: none;
    font-size: 14px; line-height: 18px; color: var(--ink);
  }
  .contact-list li { display: flex; align-items: flex-start; gap: 8px; }
  .contact-list .group { margin-bottom: 12px; }
  .contact-list svg { flex: none; margin-top: 3px; }
  .social-mark {
    flex: none; width: 11px; height: 11px; margin-top: 4px;
    background: var(--blue); border-radius: 2px;
  }
</style>
</head>
<body>
<main class="canvas">

  <section class="card card-back" aria-label="Card back">
    <div class="brand-name">Veltora</div>
    <div class="web">www.veltora-demo.com</div>
  </section>

  <section class="card card-front" aria-label="Card front">
    <div class="brand-band"><span class="brand-name">Veltora</span></div>

    <div class="role role-team">Team<br>member</div>
    <div class="role role-pm">Project<br>manager</div>
    <div class="role role-mgmt">Management</div>

    <p class="greeting">Met vriendelijke groet,</p>
    <h1 class="person-name">Marten Kuyvelsma</h1>

    <ul class="contact-list">
      <li>
        <svg width="12" height="12" viewBox="0 0 12 12" aria-hidden="true"><path d="M2.5 1h2l1 2.6-1.3 1a6 6 0 0 0 3.2 3.2l1-1.3 2.6 1v2c0 .8-.6 1.5-1.4 1.5A9.5 9.5 0 0 1 1 2.4C1 1.6 1.7 1 2.5 1z" fill="var(--orange)"/></svg>
        <span>+31 255 47 09 36</span>
      </li>
      <li class="group">
        <svg width="12" height="12" viewBox="0 0 12 12" aria-hidden="true"><rect x="3" y="0.5" width="6.5" height="11" rx="1.2" fill="none" stroke="var(--orange)" stroke-width="1.4"/><circle cx="6.25" cy="9.3" r=".8" fill="var(--orange)"/></svg>
        <span>+31 6 927 15 062</span>
      </li>
      <li class="group">
        <svg width="12" height="14" viewBox="0 0 12 14" aria-hidden="true"><path d="M6 0.5a4.5 4.5 0 0 1 4.5 4.5C10.5 8.5 6 13.5 6 13.5S1.5 8.5 1.5 5A4.5 4.5 0 0 1 6 .5z" fill="var(--orange)"/><circle cx="6" cy="5" r="1.7" fill="var(--white)"/></svg>
        <span>Oostelingpad 84c<br>2184 KT Nieuw Vennep</span>
      </li>
      <li><span class="social-mark"></span><span>marten@veltora-demo.com</span></li>
      <li><span class="social-mark"></span><span>veltora</span></li>
      <li><span class="social-mark"></span><span>@veltora</span></li>
    </ul>
  </section>

</main>
</body>
</html>
```